Guarenteed 3 page coded Wordpress Website Job*

Initial Job/budged is for 3 pages cobed wesbite only :

-Home
-Videos Production
- Animation Videos

I will require a couple of extra pages and will pay and negotiate this with the winner*

We are a video production company based in Sydney Australia specialises in tradition on site video production with camera crew, web animation videos and social media advertising. The website needs to portray a modern, sharp, young, trendy, advanced technology company and be mobile compatible. Mainly white background with colour added in banners and certain sections to lift the site. I have attached a full brief.

Target Market(s)

Small to medium businesses

Coding

Coded - Design and coding required

Number of Pages Required

3 page

Requirements
Must have
• Wordpress
• Fast loading
• Add Videos
• Add pages
• Add categories
• Sharp and professional design
• Please be creative and see breif for guide
Should not have
• NOT Cartoon looking.

```html
<!DOCTYPE html>
<html lang="en">
<head>
<meta charset="utf-8">
<title>Clearframe Media – Professional Video Solutions</title>
<link href="https://fonts.googleapis.com/css2?family=Open+Sans:wght@400;600;700;800&display=swap" rel="stylesheet">
<style>
:root{
  --blue:#1a8fd6;
  --blue-dark:#1370b0;
  --orange:#f47b20;
  --orange-dark:#d9620c;
  --ink:#333a40;
  --grey:#8a9096;
  --pale:#eef6fb;
  --teal:#0f3d45;
  --teal-dark:#0b2f36;
  --green:#3cb371;
  --white:#ffffff;
}
*{box-sizing:border-box;margin:0;padding:0}
html,body{width:1200px;height:2800px;overflow:hidden}
body{font-family:"Open Sans",Arial,sans-serif;color:var(--ink);background:var(--white);position:relative}
.page{position:relative;width:1200px;height:2800px}

/* header */
.topbar{position:absolute;top:0;left:0;width:1200px;height:60px;background:var(--white);display:flex;align-items:center;justify-content:space-between;padding:0 160px;z-index:3}
.brand{display:flex;align-items:center;gap:10px;font-weight:800;font-size:22px;color:var(--blue)}
.brand-mark{width:22px;height:22px;border-radius:50%;background:var(--orange)}
.social{display:flex;gap:8px}
.social span{width:22px;height:22px;border-radius:50%;background:var(--blue)}
.nav{position:absolute;top:60px;left:0;width:1200px;height:44px;background:rgba(10,20,30,.82);display:flex;padding:0 160px;z-index:3}
.nav a{display:block;color:#dce6ee;font-size:12px;line-height:44px;padding:0 13px;text-decoration:none;white-space:nowrap}
.nav a.active{background:var(--blue);color:var(--white)}

/* hero */
.hero{position:absolute;top:60px;left:0;width:1200px;height:540px;background:linear-gradient(90deg,#3b3d40 0%,#5a5c60 45%,#7a6c60 70%,#4b4846 100%)}
.hero-copy{position:absolute;top:180px;left:0;width:1200px;text-align:center;color:var(--white)}
.hero-copy h1{font-size:46px;font-weight:600;letter-spacing:1px;line-height:1.1}
.hero-copy p{margin-top:18px;font-size:14px}
.play{margin:16px auto 0;width:76px;height:76px;border-radius:50%;background:#e0322b;border:4px solid var(--white);display:flex;align-items:center;justify-content:center;font-weight:800;font-size:16px}
.dots{position:absolute;bottom:22px;left:0;width:1200px;display:flex;justify-content:center;gap:8px}
.dots i{width:9px;height:9px;border-radius:50%;background:rgba(255,255,255,.5)}
.dots i:first-child{background:var(--white)}

.side-tabs{position:absolute;top:560px;left:0;display:flex;flex-direction:column;gap:6px;z-index:5}
.side-tabs span{width:40px;height:40px}
.side-tabs span:nth-child(1){background:var(--orange)}
.side-tabs span:nth-child(2){background:var(--blue)}
.side-tabs span:nth-child(3){background:#3b4248}

/* welcome */
.welcome{position:absolute;top:600px;left:0;width:1200px;height:360px;text-align:center;background:linear-gradient(180deg,#fff 70%,#f2f6f9 100%)}
.section-title{font-size:30px;font-weight:600;color:var(--blue);letter-spacing:1px}
.rule{width:200px;height:2px;background:var(--orange);margin:8px auto 0}
.welcome .section-title{margin-top:60px}
.lead{width:680px;margin:16px auto 0;color:var(--orange);font-size:12px;line-height:18px}
.body{width:680px;margin:20px auto 0;color:var(--grey);font-size:12px;line-height:18px}
.btn{display:inline-block;margin-top:28px;background:var(--blue-dark);color:var(--white);font-size:13px;padding:10px 26px}

/* services */
.services{position:absolute;top:960px;left:0;width:1200px;height:680px;background:var(--pale);text-align:center}
.services .section-title{margin-top:46px}
.cards{position:absolute;top:146px;left:232px;width:736px;display:grid;grid-template-columns:356px 356px;gap:24px}
.card{height:230px;background:#2f3640;text-align:left;overflow:hidden}
.card-img{height:130px}
.card h3{background:var(--blue);color:var(--white);font-size:15px;font-weight:600;padding:6px 14px}
.card p{color:#c9d0d6;font-size:11px;line-height:16px;padding:10px 14px}

/* guarantee */
.guarantee{position:absolute;top:1660px;left:0;width:1200px;height:230px}
.guarantee-tab{position:absolute;top:0;left:140px;background:var(--orange-dark);color:var(--white);font-size:13px;padding:10px 24px}
.guarantee-band{position:absolute;top:40px;left:0;width:1200px;height:190px;background:var(--orange)}
.guarantee-band p{position:absolute;top:62px;left:180px;width:660px;color:var(--white);font-size:20px;line-height:28px}
.badge{position:absolute;top:10px;left:880px;width:170px;height:170px;border-radius:50%;background:#f9c51d;border:8px solid #1f5f9e}

/* contact */
.contact{position:absolute;top:1900px;left:0;width:1200px;height:390px;text-align:center;background:#f7f9fb}
.contact .section-title{margin-top:60px}
.contact .sub{margin-top:10px;color:var(--orange);font-size:11px;letter-spacing:1px}
.form{width:620px;margin:40px auto 0;display:grid;grid-template-columns:1fr 1fr;gap:20px 40px}
.field{height:38px;border:1px solid #d8dee3;background:var(--white);text-align:left;font-size:12px;color:#a4aab0;padding:10px 14px}
.btn-send{display:inline-block;margin-top:30px;background:var(--orange);color:var(--white);font-size:13px;font-weight:600;padding:10px 30px}

/* newsletter */
.newsletter{position:absolute;top:2290px;left:0;width:1200px;height:300px;background:var(--teal);text-align:center;color:var(--white)}
.newsletter h2{margin-top:70px;font-size:22px;font-weight:600}
.subscribe{margin:28px auto 0;display:flex;justify-content:center}
.subscribe .email{width:260px;height:36px;background:var(--white);color:#999;font-size:12px;text-align:left;padding:9px 14px;border-radius:18px 0 0 18px}
.subscribe .go{height:36px;background:var(--green);font-size:12px;font-weight:700;padding:10px 20px;border-radius:0 18px 18px 0}

/* footer */
.footer{position:absolute;top:2500px;left:0;width:1200px;height:300px;background:var(--teal-dark);color:#c6d3d6;padding:40px 150px 0;display:grid;grid-template-columns:220px 220px 200px 160px;gap:20px}
.footer h4{color:var(--white);font-size:15px;font-weight:600;margin-bottom:14px}
.footer ul{list-style:none;font-size:11px;line-height:20px}
.contact-line{display:flex;align-items:center;gap:8px;font-size:11px;line-height:22px;white-space:nowrap}
.contact-line svg{flex:none}
.follow{display:flex;gap:6px;flex-wrap:wrap;width:140px}
.follow span{width:26px;height:26px}
</style>
</head>
<body>
<div class="page">

  <section class="hero" role="img" aria-label="Photo of a cameraman filming with a professional video camera">
    <div class="hero-copy">
      <h1>PROFESSIONAL VIDEO<br>SOLUTIONS</h1>
      <p>Watch The Video</p>
      <div class="play">PLAY</div>
    </div>
    <div class="dots"><i></i><i></i><i></i></div>
  </section>

  <header class="topbar">
    <div class="brand"><span class="brand-mark"></span>Clearframe Media</div>
    <div class="social"><span></span><span></span><span></span><span></span><span></span></div>
  </header>
  <nav class="nav">
    <a class="active">Home</a><a>Video Production</a><a>Animation Videos</a><a>Social Media</a><a>Advertising Packages</a><a>Pricing</a><a>About Us</a><a>Contact Us</a>
  </nav>

  <section class="welcome">
    <h2 class="section-title">WELCOME TO OUR COMPANY!</h2>
    <div class="rule"></div>
    <p class="lead">We create sharp video content for small and medium businesses, from on site filming to web animation and social media campaigns that bring your brand to life online.</p>
    <p class="body">Our team plans, films and edits every project in house. We work closely with you from the first idea to the final cut, so your story is told clearly and your video is ready for your website, social channels and ads.</p>
    <span class="btn">Read More About Us</span>
  </section>

  <div class="side-tabs"><span></span><span></span><span></span></div>

  <section class="services">
    <h2 class="section-title">OUR SERVICES</h2>
    <div class="rule"></div>
    <div class="cards">
      <article class="card">
        <div class="card-img" role="img" aria-label="Photo of a video camera on set" style="background:linear-gradient(135deg,#2b6fa8,#9fc3dd)"></div>
        <h3>video production</h3>
        <p>On site filming with full crew, lighting and sound. We shoot, edit and deliver polished videos ready to share.</p>
      </article>
      <article class="card">
        <div class="card-img" role="img" aria-label="Photo of a camera crew filming" style="background:linear-gradient(135deg,#3a4450,#8d97a2)"></div>
        <h3>camera crew</h3>
        <p>Experienced operators for events, interviews and promos. Book a crew for a half day, full day or longer.</p>
      </article>
      <article class="card">
        <div class="card-img" role="img" aria-label="Image of an office team at work" style="background:linear-gradient(135deg,#6fa7c9,#d7c49a)"></div>
        <h3>web animation videos</h3>
        <p>Clear animated explainers that show what you do in under two minutes, made to suit your brand and audience.</p>
      </article>
      <article class="card">
        <div class="card-img" role="img" aria-label="Image of social media icons on a grid" style="background:linear-gradient(135deg,#3d6fb6,#a9c6e6)"></div>
        <h3>social media advertising</h3>
        <p>Short video ads built for social feeds, with targeting and reporting to help you reach new customers.</p>
      </article>
    </div>
  </section>

  <section class="guarantee">
    <div class="guarantee-band">
      <p>All our video production packages come with a full money back guarantee! *when the work hasn't been seen by you</p>
      <div class="badge" role="img" aria-label="Money back guarantee badge"></div>
    </div>
    <div class="guarantee-tab">The money back guarantee</div>
  </section>

  <section class="contact">
    <h2 class="section-title">GET IN TOUCH</h2>
    <div class="rule"></div>
    <p class="sub">WANT TO SPEAK TO OUR TEAM ABOUT YOUR NEXT VIDEO?</p>
    <div class="form">
      <div class="field">Your name</div>
      <div class="field">Your phone number</div>
      <div class="field">Your email address</div>
      <div class="field">Type your message here</div>
    </div>
    <span class="btn-send">SEND TO CONSULTANT</span>
  </section>

  <section class="newsletter">
    <h2>Subscribe to our newsletter</h2>
    <div class="subscribe"><div class="email">your@email.com</div><div class="go">SUBSCRIBE</div></div>
  </section>

  <footer class="footer">
    <div>
      <h4>Site Map</h4>
      <ul><li>Home</li><li>Video Production</li><li>Animation Videos</li><li>Social Media</li><li>Pricing Packages</li><li>Frequently Asked</li></ul>
    </div>
    <div>
      <ul style="margin-top:33px"><li>Portfolio</li><li>Camera Crew</li><li>Corporate</li><li>Events</li><li>Testimonials</li><li>Our Blog</li></ul>
    </div>
    <div>
      <h4>Contact info</h4>
      <div class="contact-line"><svg width="12" height="12" viewBox="0 0 12 12"><rect x="1" y="2" width="10" height="8" fill="none" stroke="#c6d3d6"/><path d="M1 2l5 4 5-4" fill="none" stroke="#c6d3d6"/></svg>hello@clearframe.example</div>
      <div class="contact-line"><svg width="12" height="12" viewBox="0 0 12 12"><path d="M3 1l2 3-1 1c1 2 2 3 4 4l1-1 3 2-1 2C6 12 0 6 1 2z" fill="#c6d3d6"/></svg>000 000 000</div>
      <div class="contact-line"><svg width="12" height="12" viewBox="0 0 12 12"><path d="M6 11C3 7 2 5.5 2 4a4 4 0 018 0c0 1.5-1 3-4 7z" fill="#c6d3d6"/></svg>12 Sample Street, Sydney</div>
    </div>
    <div>
      <h4>Follow us on</h4>
      <div class="follow"><span style="background:#3b5998"></span><span style="background:#1da1f2"></span><span style="background:#dd4b39"></span><span style="background:#0077b5"></span><span style="background:#e1306c"></span></div>
    </div>
  </footer>

</div>
</body>
</html>
```